Community Legal Website

The website is about a law in legal area (Fiscal), it has a moderator and the community also contributes with information.

Attention that this is not for a Law Firm. This is a community site where all the lawyers can contribute wiith their knowledge and at the same time where they can read the Official Law in the fiscal area.

The site is in portuguese, but we have attach information in english about the functionalities.

I attach information which represents the first version of the site done by html.. That is the site we intend to improve.

The site is quite simple because the main pages are:
- Home page;
- Section page (which has the Chapters and articles)
- Article page;

This pages all belong to the article:

redaccao_actual.htm, redaccoes_anteriores.htm, anotacoes.htm, jurisprudencia.htm, decisoesadministrativas.htm, minutas.htm, duvidas.htm

AS you see in all of them the options are always there.

The most important in this site is the usability of the content:

The FAQ, Contacts, Terms of conditions, who we are, are links less important.

Also there is a possibility to have in the homepage a higligh of certain articles that we want to raise from the others.

Please check the excel sheet as well as the zip file wich has the site in portuguese that you can use a website translator to check in your language.
Updates

We added a excel sheet with the functionalities in english which the site must have.

Reason: Because this is easter time we have increased the time for the deliver

Please check briefing update.

Reason: There were some request to extend the deadline because of the Easter

Hi!

Please read carefully the briefing. People are presenting me company web sites adn this is NOT a company web site. THis is a Site wich has a content of Laws. Please check the 1st version in the zip file and improve it. The options are there and you can translate in google tradutor or reading the excel sheet attach.

txs,
JV

Reason: My client need more desing choices

Target Market(s)

Lawyers, jurists and people related with the fiscal Law.

Industry/Entity Type

Legal

Requirements
Must have
• The interface should be clean and elegant.
It should also contribute to speed.
And try to avoid to many distract elements.
The site will be dinamic and with a backoffice, so in that you have to be carefully with the space dynamic. But you don't have to worry about the backoffice. Only the front office which is the public site.

```html
<!DOCTYPE html>
<html lang="pt">
<head>
<meta charset="utf-8">
<title>Legislação Anotada</title>
<link href="https://fonts.googleapis.com/css2?family=Open+Sans:ital,wght@0,400;0,600;0,700;1,600&display=swap" rel="stylesheet">
<style>
  :root {
    --top-bar: #dcdcdc;
    --tab: #8fb1ab;
    --ink: #1f1f1f;
    --teal: #4f7d74;
    --teal-dark: #44706a;
    --teal-light: #6f9a91;
    --row: #eff5f4;
    --row-active: #d8e7e4;
    --row-line: #ffffff;
    --footer: #ebebeb;
    --footer-text: #7a7a7a;
  }
  * { box-sizing: border-box; margin: 0; padding: 0; }
  html, body { width: 1200px; height: 688px; overflow: hidden; }
  body {
    font-family: "Open Sans", Arial, sans-serif;
    background: #fff;
    position: relative;
    color: var(--ink);
  }
  .top-bar { position: absolute; left: 0; top: 0; width: 1200px; height: 6px; background: var(--top-bar); }
  .contact-tab {
    position: absolute; left: 928px; top: 0; width: 144px; height: 25px;
    background: var(--tab);
    clip-path: polygon(8px 0, 100% 0, calc(100% - 8px) 100%, 0 100%);
    color: #fff; font-style: italic; font-weight: 600; font-size: 13px;
    text-align: center; line-height: 26px; text-decoration: none;
  }
  .brand { position: absolute; left: 134px; top: 86px; display: flex; align-items: center; gap: 14px; }
  .brand-mark { width: 26px; height: 26px; background: var(--teal); }
  .brand-name { font-size: 17px; color: var(--ink); letter-spacing: 0.2px; }
  .main-nav { position: absolute; top: 56px; left: 555px; height: 76px; display: flex; }
  .main-nav a {
    display: block; font-size: 14px; color: var(--ink); text-decoration: none;
    line-height: 86px; padding: 0 12px;
  }
  .main-nav a.active { color: var(--teal); }
  .nav-sep { width: 22px; height: 76px; }
  .column {
    position: absolute; top: 172px; width: 478px; height: 418px;
    background: linear-gradient(90deg, rgba(0,0,0,0.07), rgba(0,0,0,0) 22px);
  }
  .column::after {
    content: ""; position: absolute; inset: 0;
    background: linear-gradient(180deg, #fff 0, rgba(255,255,255,0) 40px, rgba(255,255,255,0) 360px, #fff 100%);
    pointer-events: none;
  }
  .column.fiscal { left: 110px; }
  .column.admin { left: 611px; }
  .panel-head {
    position: absolute; top: 48px; left: 0; width: 478px; height: 51px;
    background: linear-gradient(180deg, var(--teal-light), var(--teal) 45%, var(--teal-dark));
    color: #fff; font-size: 20px; padding-left: 32px; line-height: 52px; letter-spacing: 0.2px;
    z-index: 1;
  }
  .panel-head svg { position: absolute; right: 14px; top: 10px; }
  .law-list { position: absolute; top: 101px; left: 0; width: 478px; list-style: none; z-index: 1; }
  .law-list li {
    background: var(--row); height: 56px; border-bottom: 1px solid var(--row-line);
    padding: 9px 0 0 36px; position: relative; font-size: 13px; line-height: 16px; color: var(--teal);
  }
  .law-list li.active { background: var(--row-active); text-decoration: underline; }
  .law-list li svg { position: absolute; left: 19px; top: 12px; }
  .law-list .code { font-weight: 700; color: var(--teal-dark); display: block; }
  .site-footer {
    position: absolute; left: 0; top: 607px; width: 1200px; height: 81px;
    background: var(--footer); box-shadow: inset 0 3px 4px -2px rgba(0,0,0,0.18);
    text-align: center; font-size: 12.5px; color: var(--footer-text); line-height: 78px;
    padding-left: 0; text-indent: -14px;
  }
</style>
</head>
<body>
  <div class="top-bar"></div>
  <a class="contact-tab" href="#">CONTACTOS</a>

  <div class="brand">
    <span class="brand-mark"></span>
    <span class="brand-name">NUNES TAVARES.net</span>
  </div>

  <nav class="main-nav">
    <a href="#">TERMOS DE UTILIZAÇÃO</a>
    <svg class="nav-sep" viewBox="0 0 22 76"><defs><linearGradient id="sg" x1="0" x2="1"><stop offset="0" stop-color="#000" stop-opacity="0.09"/><stop offset="1" stop-color="#000" stop-opacity="0"/></linearGradient></defs><polygon points="20,0 22,0 2,76 0,76" fill="url(#sg)"/><polygon points="20,0 2,76 16,76" fill="url(#sg)" opacity="0.6"/></svg>
    <a href="#" class="active">PERGUNTAS FREQUENTES</a>
    <svg class="nav-sep" viewBox="0 0 22 76"><polygon points="20,0 22,0 2,76 0,76" fill="url(#sg)"/><polygon points="20,0 2,76 16,76" fill="url(#sg)" opacity="0.6"/></svg>
    <a href="#">QUEM SOMOS</a>
  </nav>

  <section class="column fiscal">
    <h2 class="panel-head" style="font-weight:400">LEGISLAÇÃO FISCAL ANOTADA
      <svg width="34" height="30" viewBox="0 0 34 30"><g fill="none" stroke="#e8f0ee" stroke-width="1.6"><rect x="3" y="10" width="5" height="15"/><rect x="10" y="4" width="5" height="21"/><rect x="17" y="13" width="5" height="12"/><rect x="24" y="8" width="5" height="17"/><line x1="1" y1="28" x2="33" y2="28"/></g></svg>
    </h2>
    <ul class="law-list">
      <li><svg width="10" height="11" viewBox="0 0 10 11"><path d="M1 .5h6l2 2v8H1z M3 4h4 M3 6h4 M3 8h4" fill="none" stroke="#7a8f8b"/></svg><span class="code">Código do IRS</span>Imposto sobre o Rendimento das Pessoas Singulares</li>
      <li class="active"><svg width="10" height="11" viewBox="0 0 10 11"><path d="M1 .5h6l2 2v8H1z M3 4h4 M3 6h4 M3 8h4" fill="none" stroke="#7a8f8b"/></svg><span class="code">Código do IRC</span>Imposto sobre o Rendimento das Pessoas Colectivas</li>
      <li><svg width="10" height="11" viewBox="0 0 10 11"><path d="M1 .5h6l2 2v8H1z M3 4h4 M3 6h4 M3 8h4" fill="none" stroke="#7a8f8b"/></svg><span class="code">Código do IMI</span>Imposto Municipal sobre Imóveis</li>
      <li><svg width="10" height="11" viewBox="0 0 10 11"><path d="M1 .5h6l2 2v8H1z M3 4h4 M3 6h4 M3 8h4" fill="none" stroke="#7a8f8b"/></svg><span class="code">RCPIT</span>Regulamento Complementar do Procedimento de Inspecção Tributária</li>
    </ul>
  </section>

  <section class="column admin">
    <h2 class="panel-head" style="font-weight:400">LEGISLAÇÃO ADMINISTRATIVA ANOTADA
      <svg width="30" height="32" viewBox="0 0 30 32"><rect x="1.5" y="1.5" width="27" height="29" rx="4" fill="none" stroke="#e8f0ee" stroke-width="1.6"/><g stroke="#e8f0ee" stroke-width="1.6"><line x1="6" y1="8" x2="9" y2="8"/><line x1="11" y1="8" x2="24" y2="8"/><line x1="6" y1="13" x2="9" y2="13"/><line x1="11" y1="13" x2="24" y2="13"/><line x1="6" y1="18" x2="9" y2="18"/><line x1="11" y1="18" x2="24" y2="18"/><line x1="6" y1="23" x2="9" y2="23"/><line x1="11" y1="23" x2="24" y2="23"/></g></svg>
    </h2>
    <ul class="law-list">
      <li><svg width="10" height="11" viewBox="0 0 10 11"><path d="M1 .5h6l2 2v8H1z M3 4h4 M3 6h4 M3 8h4" fill="none" stroke="#7a8f8b"/></svg><span class="code">CPTA</span>Código do Procedimento nos Tribunais Administrativos</li>
    </ul>
  </section>

  <footer class="site-footer">(c) NUNES TAVARES - 2013</footer>
</body>
</html>
```